Etiketten für Honig
Zielgruppe
Hobby-Imkerei / Verkauf von Honig - eigene Völker ( Produktion)
Zielgruppe: Privatpersonen (Freunde, Bekannte) keine Zwischenhändler
Aufgabenstellung
Ich wohne in einem alten Fachwerkhaus, welches ursprünglich als Schmiede gebaut wurde.
Honig& Schmiede oder Biene & Schmiede sollten berücksichtigt werden
Stichwort: Schmiedehonig oder so ähnlich
Etiketten mit Verbraucherschutz
Ursprung Deutschland
Gläser: Neutral
Abmessungen:
•Durchmesser: 8,05 cm
•Gesamthöhe: 9,4 cm
•Höhe ohne Gewinde: 8,05 cm

```html
<!DOCTYPE html>
<html lang="de">
<head>
<meta charset="utf-8">
<title>Wabenesse – Etikett</title>
<link rel="stylesheet" href="https://fonts.googleapis.com/css2?family=Libre+Caslon+Text:wght@400&display=swap">
<style>
  :root {
    --bg: #efe9df;
    --paper: #fbfaf6;
    --ink: #141414;
    --seal-red: #e2283c;
    --ornament: #8a1a24;
    --shadow: rgba(0,0,0,0.12);
  }
  html, body {
    margin: 0;
    width: 1200px;
    height: 1200px;
    overflow: hidden;
    background: var(--bg);
  }
  .canvas {
    position: relative;
    width: 1200px;
    height: 1200px;
  }
  .main-label {
    position: absolute;
    left: 60px;
    top: 200px;
    width: 1080px;
    height: 460px;
    background: var(--paper);
    box-shadow: 0 4px 16px var(--shadow);
    display: flex;
    color: var(--ink);
  }
  .front-panel {
    width: 620px;
    display: flex;
    flex-direction: column;
    align-items: center;
    padding-top: 70px;
    box-sizing: border-box;
  }
  .product-name {
    font-family: "Libre Caslon Text", serif;
    font-weight: 400;
    font-size: 66px;
    line-height: 1;
    margin: 0;
  }
  .connector {
    font-family: "Libre Caslon Text", serif;
    font-size: 42px;
    margin: 16px 0 8px;
  }
  .apiary-name {
    font-family: "Libre Caslon Text", serif;
    font-weight: 400;
    font-size: 80px;
    line-height: 1.1;
    margin: 0;
  }
  .net-weight {
    font-family: "Libre Caslon Text", serif;
    font-size: 30px;
    margin-top: auto;
    margin-bottom: 36px;
  }
  .info-panel {
    flex: 1;
    padding: 80px 50px 0 40px;
    font-family: "Libre Caslon Text", serif;
    font-size: 22px;
    line-height: 1.45;
    text-align: center;
  }
  .info-panel p { margin: 0 0 14px; }
  .seal-strip {
    position: absolute;
    left: 60px;
    top: 780px;
    width: 1080px;
    height: 96px;
    background: var(--seal-red);
    box-shadow: 0 4px 12px var(--shadow);
    display: flex;
    align-items: center;
    justify-content: space-around;
  }
  .seal-ornament {
    width: 54px;
    height: 60px;
  }
  .seal-variety {
    font-family: "Libre Caslon Text", serif;
    font-size: 30px;
    color: var(--ink);
  }
</style>
</head>
<body>
<main class="canvas">
  <section class="main-label">
    <div class="front-panel">
      <h1 class="product-name">Bienenhonig</h1>
      <div class="connector">aus der</div>
      <h2 class="apiary-name">Wabenesse</h2>
      <div class="net-weight">500 gr</div>
    </div>
    <div class="info-panel">
      <p>Dieses Glas enthält 500 g naturbelassenen Bienenhonig aus der Imkerei von</p>
      <p>Jonas Feldrain<br>Lindenweg 4<br>54321 Heidbach<br>0987-654321</p>
      <p>Kühl, trocken und dunkel gelagert ist dieser Honig mindestens haltbar bis:</p>
    </div>
  </section>

  <section class="seal-strip">
    <svg class="seal-ornament" role="img" aria-label="Ornament" viewBox="0 0 54 60"><rect width="54" height="60" rx="8" fill="var(--ornament)" opacity="0.45"/></svg>
    <span class="seal-variety">Sommerblütenhonig</span>
    <svg class="seal-ornament" role="img" aria-label="Ornament" viewBox="0 0 54 60"><rect width="54" height="60" rx="8" fill="var(--ornament)" opacity="0.45"/></svg>
  </section>
</main>
</body>
</html>
```